Brivond Technologies business card design

We need a business card designed with our new logo. it would be great if the card could communicate it is a technology based company.

Target Market(s)

system integrators

Industry/Entity Type

technology, IOT

Contact Information for Business Card

Name, designation, Address, telephone number, email address

Requirements
Must have
• logo and company name
Nice to have
• something to do with technology

```html
<!DOCTYPE html>
<html lang="en">
<head>
<meta charset="utf-8">
<title>Brivond Technologies – Business Card</title>
<link href="https://fonts.googleapis.com/css2?family=Arimo:wght@400;700&display=swap" rel="stylesheet">
<style>
  :root {
    --backdrop: #d4d3cf;
    --card: #353535;
    --card-deep: #222222;
    --card-soft: #5c5c5c;
    --accent: #f7941d;
    --ink-light: #ffffff;
    --ink-muted: #e6e6e6;
  }
  * { margin: 0; padding: 0; box-sizing: border-box; }
  html, body {
    width: 1200px; height: 801px; overflow: hidden;
    background: var(--backdrop);
    font-family: "Arimo", Arial, sans-serif;
  }
  .stage {
    position: relative; width: 1200px; height: 801px;
    display: flex; align-items: center; justify-content: center; gap: 40px;
  }
  .card {
    position: relative; width: 540px; height: 309px;
    background: var(--card);
    border-bottom: 5px solid var(--accent);
    border-left: 3px solid var(--accent);
    box-shadow: 0 10px 24px rgba(0,0,0,0.25);
    overflow: hidden;
  }
  .brand {
    position: absolute; display: flex; align-items: center; gap: 10px;
    color: var(--ink-light); font-weight: 700; letter-spacing: 1px;
    text-transform: uppercase; white-space: nowrap;
  }
  .brand-mark { width: 14px; height: 14px; background: var(--accent); flex: none; }
  .card-front .brand { top: 52px; left: 50%; transform: translateX(-38%); font-size: 22px; }
  .person { position: absolute; left: 64px; top: 128px; }
  .person-name { color: var(--accent); font-weight: 700; font-size: 21px; letter-spacing: 0.5px; text-transform: uppercase; }
  .person-role { color: var(--ink-muted); font-size: 14px; margin-top: 4px; }
  .address {
    position: absolute; right: 48px; top: 134px; text-align: right;
    color: var(--ink-muted); font-size: 14px; line-height: 20px; font-style: normal;
  }
  .divider {
    position: absolute; left: 64px; right: 48px; top: 188px;
    height: 1px; background: var(--accent);
  }
  .contacts { position: absolute; left: 64px; top: 202px; list-style: none; }
  .contacts li {
    display: flex; align-items: center; gap: 8px;
    color: var(--ink-muted); font-size: 14px; line-height: 22px;
  }
  .contacts svg { width: 11px; height: 11px; fill: var(--accent); flex: none; }
  .mark-area {
    position: absolute; left: 24px; top: 28px; width: 270px; height: 270px;
    background:
      linear-gradient(160deg, var(--card-soft) 0%, rgba(53,53,53,0) 45%),
      radial-gradient(circle at 50% 60%, var(--card-deep) 0%, var(--card) 72%);
    opacity: 0.9;
  }
  .card-back .brand { right: 34px; bottom: 74px; font-size: 28px; }
</style>
</head>
<body>
<main class="stage">
  <section class="card card-front" aria-label="Card front">
    <div class="brand"><span class="brand-mark"></span>Brivond Technologies</div>
    <div class="person">
      <div class="person-name">Daniel Marsh</div>
      <div class="person-role">CEO/Founder</div>
    </div>
    <address class="address">2180 Harbor Lane<br>Northfield AB 4021</address>
    <div class="divider"></div>
    <ul class="contacts">
      <li><svg viewBox="0 0 12 12"><path d="M2 1h3l1 3-1.5 1a7 7 0 0 0 2.5 2.5L8 6l3 1v3a1 1 0 0 1-1 1A9 9 0 0 1 1 2a1 1 0 0 1 1-1z"/></svg>(555) 014-3827</li>
      <li><svg viewBox="0 0 12 12"><path d="M1 2h10v8H1z M1 2l5 4 5-4" stroke="#353535" stroke-width="1"/></svg>info@brivondtech.com</li>
      <li><svg viewBox="0 0 12 12"><circle cx="6" cy="6" r="5"/><path d="M1 6h10M6 1v10" stroke="#353535" stroke-width="0.8"/></svg>www.brivondtech.com</li>
    </ul>
  </section>
  <section class="card card-back" aria-label="Card back">
    <div class="mark-area" role="img" aria-label="Large faint brand mark decoration"></div>
    <div class="brand">Brivond Technologies</div>
  </section>
</main>
</body>
</html>
```